Business Card for Marco Tindley Analytics and Marco Tindley Photography

I want a double sided business card: on one side it should be about "Marco Tindley Photography" and on the other side about "Marco Tindley Analytics". You find the logos for these two projects in the attachments. The design of the business card should blend well with the colours and fonts used in the logos and should be quite simple, yet look professional and modern.

In addition to my name, there should be content for a telephone number, e-mail address and website. There should be little icons (for telephone, email and web) before these fields. I do not want a postal mail address field.
Lastly you should indicate that people can contact me in the following languages: Lëtzebuergesch, Deutsch, Français, English, Castellano, Ido
This should be very unobtrusive: either in a small muted font or with little icons (preferably without using flags as flags represent nations, not languages - one possibility would be by using the 2 letter ISO codes).

The design should be delivered in Adobe Illustrator format or something similar that I can edit easily, as it's possible that I will change my e-mail address and domain soon.

I hope this was detailed enough but still leaves you some freedom for designing something nice.

Thank you!
Marco

Industry/Entity Type

Business

Contact Information for Business Card

e-mail address: mjt_@fernpost.example
website: www.marcotindley.example (for Marco Tindley Photography)
website: quarrynet.example/mjt (for Marco Tindley Analytics - this address is likely to change)
phone: +352 648 907 215 (not my real number - I prefer not to publish it on the web)

Requirements
Nice to have
• A speech bubble followed by the 2-letter language codes (lb, de, fr, en, es, io) or even speech bubble icons for every language would be nice and eliminates the need to put text like 'you can contact me in the following languages'.

```html
<!DOCTYPE html>
<html lang="en">
<head>
<meta charset="utf-8">
<title>Marco Tindley Business Cards</title>
<link rel="stylesheet" href="https://fonts.googleapis.com/css2?family=Lato:wght@400;700&display=swap">
<style>
  :root {
    --bg: #2b2b2b;
    --black: #050505;
    --blue: #26a3dd;
    --orange: #f28322;
    --green: #45b44a;
    --white: #ffffff;
    --ink: #141414;
  }
  html, body { margin: 0; padding: 0; overflow: hidden; }
  body {
    width: 1200px; height: 880px;
    background: var(--bg);
    position: relative;
    font-family: "Lato", sans-serif;
  }
  .card {
    position: absolute;
    width: 620px; height: 354px;
    box-shadow: 0 18px 40px rgba(0,0,0,.45);
    overflow: hidden;
  }
  .card--photography { left: 60px; top: 60px; }
  .card--analytics { left: 520px; top: 466px; }
  .card__art { position: absolute; inset: 0; width: 100%; height: 100%; }
  .brand {
    position: absolute;
    left: 60px; top: 118px;
    font-size: 28px; font-weight: 700;
    line-height: 1.15;
    margin: 0;
    color: var(--orange);
  }
  .contacts {
    position: absolute;
    right: 22px; top: 74px;
    list-style: none; margin: 0; padding: 0;
    text-align: right;
    color: var(--ink);
    font-size: 14px;
  }
  .contacts li {
    display: flex; align-items: center; justify-content: flex-end;
    gap: 8px; height: 21px;
  }
  .contacts svg { width: 14px; height: 14px; flex: none; }
  .languages {
    position: absolute;
    left: 196px; top: 306px;
    display: flex; align-items: center; gap: 8px;
    color: var(--ink);
    font-size: 13px;
    margin: 0;
  }
  .languages svg { width: 20px; height: 18px; flex: none; }
</style>
</head>
<body>

<section class="card card--photography">
  <svg class="card__art" viewBox="0 0 620 354" preserveAspectRatio="none" aria-hidden="true">
    <rect width="620" height="354" fill="var(--black)"/>
    <path d="M0 262 C230 236 370 150 420 0 L434 0 C394 160 246 286 0 326 Z" fill="var(--orange)"/>
    <path d="M440 0 L620 0 L620 354 L0 354 L0 334 C250 290 400 160 440 0 Z" fill="var(--blue)"/>
  </svg>
  <h1 class="brand">Marco Tindley<br>Photography</h1>
  <ul class="contacts">
    <li>+352 648 907 215
      <svg viewBox="0 0 16 16"><path d="M2 6c0-3 12-3 12 0v1h-3V5.5H5V7H2z M4 8h8l1 6H3z" fill="var(--ink)"/></svg></li>
    <li>mjt_@fernpost.example
      <svg viewBox="0 0 16 16"><rect x="1" y="3" width="14" height="10" fill="var(--ink)"/><path d="M1 3l7 6 7-6" stroke="#fff" stroke-width="1.2" fill="none"/></svg></li>
    <li>www.marcotindley.example
      <svg viewBox="0 0 16 16"><circle cx="8" cy="8" r="6.5" fill="none" stroke="var(--ink)" stroke-width="1.4"/><path d="M1.5 8h13M8 1.5c-3 3.5-3 9.5 0 13M8 1.5c3 3.5 3 9.5 0 13" stroke="var(--ink)" stroke-width="1.1" fill="none"/></svg></li>
  </ul>
  <p class="languages">
    <svg viewBox="0 0 20 18"><ellipse cx="10" cy="8" rx="9" ry="7" fill="var(--ink)"/><path d="M13 13l5 4-8-2z" fill="var(--ink)"/></svg>
    Lëtzebuergesch | Deutsch | Français | English | Castellano | Ido
  </p>
</section>

<section class="card card--analytics">
  <svg class="card__art" viewBox="0 0 620 354" preserveAspectRatio="none" aria-hidden="true">
    <rect width="620" height="354" fill="var(--white)"/>
    <path d="M0 262 C230 236 370 150 420 0 L434 0 C394 160 246 286 0 326 Z" fill="var(--orange)"/>
    <path d="M440 0 L620 0 L620 354 L0 354 L0 334 C250 290 400 160 440 0 Z" fill="var(--green)"/>
  </svg>
  <h1 class="brand">Marco Tindley<br>Analytics</h1>
  <ul class="contacts">
    <li>+352 648 907 215
      <svg viewBox="0 0 16 16"><path d="M2 6c0-3 12-3 12 0v1h-3V5.5H5V7H2z M4 8h8l1 6H3z" fill="var(--ink)"/></svg></li>
    <li>mjt_@fernpost.example
      <svg viewBox="0 0 16 16"><rect x="1" y="3" width="14" height="10" fill="var(--ink)"/><path d="M1 3l7 6 7-6" stroke="#fff" stroke-width="1.2" fill="none"/></svg></li>
    <li>quarrynet.example/mjt
      <svg viewBox="0 0 16 16"><circle cx="8" cy="8" r="6.5" fill="none" stroke="var(--ink)" stroke-width="1.4"/><path d="M1.5 8h13M8 1.5c-3 3.5-3 9.5 0 13M8 1.5c3 3.5 3 9.5 0 13" stroke="var(--ink)" stroke-width="1.1" fill="none"/></svg></li>
  </ul>
  <p class="languages">
    <svg viewBox="0 0 20 18"><ellipse cx="10" cy="8" rx="9" ry="7" fill="var(--ink)"/><path d="M13 13l5 4-8-2z" fill="var(--ink)"/></svg>
    Lëtzebuergesch | Deutsch | Français | English | Castellano | Ido
  </p>
</section>

</body>
</html>
```